Relationship Seminar

I am an Author and Speaker and I need a flyer for a Christian relationship seminar targeting women aged between mid 20's to late 30's. It's an event for women only.

-I am looking for a fresh/ edgy look but still feminine
-Nothing too girly
-Maximum of 3 colours (Spring colours are good)
-I want the flyer to convey joy or happiness
-Use my photo which is attached as the predominant image (you can crop it to remove the background etc)

The Flyer Details are as follows:

Somewhere Past Tomorrow - Brisbane Tour

Join Author & Speaker, Rosalind Okafe, as she speaks about her new book entitled 'Somewhere Past Tomorrow'.

Be inspired and encouraged to embrace the life that God has given you and make the most of it!

Date: Saturday 9th November 2013
Time: 2:00 pm - 5:00 pm
Location: Larkwell Hotel Brisbane (Juniper Ballroom)
Fennimore Street, Brisbane QLD 4000
Tickets: $60/pp (Includes High Tea)
Buy Tickets: www.rosalindokafe.com or http://somewherepasttomorrow.ticketvane.net

Email: info@rosalindokafe.com

Include the cover of my new book.

www.rosalindokafe.com (include my website at the bottom of the flyer)

Target Market(s)

Young professional women aged between their mid 20's to late 30's

Industry/Entity Type

Event

Requirements
Should not have
• -No girly or curly font

```html
<!DOCTYPE html>
<html lang="en">
<head>
<meta charset="utf-8">
<title>Somewhere Past Tomorrow – Brisbane Tour</title>
<link rel="stylesheet" href="https://fonts.googleapis.com/css2?family=Cinzel:wght@400;600;700&family=Open+Sans:wght@400;700&display=swap">
<style>
  :root {
    --orange: #f26a1b;
    --green: #8cc63e;
    --ink: #1a1a1a;
    --paper: #ffffff;
    --backdrop: #f4f3f1;
    --brick: #c98f7a;
    --brick-light: #ece3dc;
    --hair: #2e2220;
  }
  * { margin: 0; padding: 0; box-sizing: border-box; }
  html, body {
    width: 1200px; height: 848px; overflow: hidden;
    background: var(--backdrop);
  }
  .flyer {
    position: absolute; left: 256px; top: 194px;
    width: 689px; height: 459px;
    background: var(--paper);
    font-family: "Open Sans", Arial, sans-serif;
    color: var(--ink);
    overflow: hidden;
  }
  .hero-photo {
    position: absolute; left: 334px; top: 0;
    width: 355px; height: 151px;
    background:
      radial-gradient(ellipse 100px 140px at 250px 110px, var(--hair) 0%, rgba(46,34,32,0.6) 50%, transparent 80%),
      linear-gradient(90deg, var(--paper) 0%, var(--brick-light) 25%, var(--brick) 70%, #b8806c 100%);
  }
  .title {
    position: absolute; left: 4px; top: 20px; width: 340px;
    text-align: center;
    font-family: "Cinzel", "Trajan Pro", serif;
    font-weight: 600;
    color: var(--orange);
    line-height: 1;
    white-space: nowrap;
  }
  .title .line-one { display: block; font-size: 37px; }
  .title .line-two { display: block; font-size: 33px; margin-top: 10px; }
  .title .tour {
    display: block; font-size: 22px; color: var(--green);
    margin-top: 12px;
  }
  .intro {
    position: absolute; left: 20px; top: 153px; width: 660px;
    font-size: 14.3px; font-weight: 700; line-height: 23px;
    text-indent: 22px;
  }
  .intro .speaker {
    font-family: "Cinzel", serif; font-weight: 700;
    color: var(--orange); font-size: 16.5px;
  }
  .book-cover {
    position: absolute; left: 52px; top: 231px;
    width: 122px; height: 180px;
    background: linear-gradient(160deg, #f7f4f0 0%, #e6e1db 60%, #cfd9c0 100%);
    box-shadow: 2px 3px 6px rgba(0,0,0,0.25);
  }
  .details {
    position: absolute; left: 222px; top: 236px;
    border-collapse: collapse;
    font-size: 16px; line-height: 21.5px;
  }
  .details th {
    text-align: left; vertical-align: top;
    color: var(--green); font-weight: 700;
    width: 100px; white-space: nowrap;
  }
  .details td { white-space: nowrap; }
  .web-band {
    position: absolute; left: 0; bottom: 0;
    width: 100%; height: 36px;
    background: var(--orange);
    color: var(--paper);
    font-family: "Cinzel", serif; font-weight: 600;
    font-size: 24px; line-height: 38px;
    text-align: center;
    letter-spacing: 0.5px;
  }
</style>
</head>
<body>
  <main class="flyer">
    <div class="hero-photo" role="img" aria-label="Photo of the author smiling in front of a whitewashed brick wall"></div>

    <h1 class="title">
      <span class="line-one">Somewhere</span>
      <span class="line-two">Past Tomorrow</span>
      <span class="tour">Brisbane Tour</span>
    </h1>

    <p class="intro">Join Author &amp; Speaker, <span class="speaker">Rosalind Okafe</span>, as she speaks about her new book entitled 'Somewhere Past Tomorrow'. Be inspired and encouraged to embrace the life that God has given you and make the most of it!</p>

    <div class="book-cover" role="img" aria-label="Cover of the book Somewhere Past Tomorrow showing the author between two men"></div>

    <table class="details">
      <tr><th>Date:</th><td>Saturday 9th November 2013</td></tr>
      <tr><th>Time:</th><td>2:00 pm - 5:00 pm</td></tr>
      <tr><th>Location:</th><td>Larkwell Hotel Brisbane (Juniper Ballroom)<br>Fennimore Street, Brisbane QLD 4000</td></tr>
      <tr><th>Tickets:</th><td>$60/pp (Includes High Tea)</td></tr>
      <tr><th>Buy Tickets:</th><td>www.rosalindokafe.com or<br>http://somewherepasttomorrow.ticketvane.net</td></tr>
      <tr><th>Email:</th><td>info@rosalindokafe.com</td></tr>
    </table>

    <footer class="web-band">www.rosalindokafe.com</footer>
  </main>
</body>
</html>
```